New Website Design. Porjtect is Guaranteed.

I would like a site similar to this: http://givevehiclehope.org.

old site: http://www.wheelsforbloom.org

Create a professional website; a car donation site seeking leads to return calls.

Please see http://givevehiclehope.org for the concept I am after.

The webpage should have a professional feel. The pages to include are 'Home', 'About us' and 'Get Started'

Industry/Entity Type

It Professional

Coding

Coded - Design and coding required

Number of Pages Required

1 page

```html
<!DOCTYPE html>
<html lang="en">
<head>
<meta charset="utf-8">
<title>Give Vehicle Hope</title>
<link rel="stylesheet" href="https://fonts.googleapis.com/css2?family=Raleway:wght@300;400;500;600;700&family=Open+Sans:wght@400;600&display=swap">
<style>
:root{
  --nav:#363636;
  --blue:#2f64b1;
  --blue-bright:#4b8be8;
  --ink:#4a4a4a;
  --muted:#6a6a6a;
  --line:#dcdcdc;
  --white:#ffffff;
  --panel:#f3f3f3;
}
*{box-sizing:border-box;margin:0;padding:0}
html,body{width:896px;height:1200px;overflow:hidden;background:var(--white)}
body{position:relative;font-family:"Raleway",sans-serif;color:var(--ink)}
.site-nav{position:absolute;left:0;top:0;width:896px;height:60px;background:var(--nav)}
.brand{position:absolute;left:84px;top:16px;font-weight:600;font-size:20px;color:var(--white);letter-spacing:.2px}
.menu{position:absolute;left:308px;top:24px;display:flex;gap:47px;font-size:10px;letter-spacing:1px;color:#cfcfcf}
.nav-cta{position:absolute;left:704px;top:14px;width:107px;height:31px;border:2px solid var(--white);background:var(--blue);color:var(--white);font-size:10px;font-weight:700;letter-spacing:1px;display:flex;align-items:center;justify-content:center}
.hero{position:absolute;left:0;top:60px;width:896px;height:354px}
.hero-photo{position:absolute;inset:0;background:linear-gradient(100deg,#7a6c64 0%,#b9ada4 30%,#6f6661 52%,#cfcbca 75%,#9aa0a8 100%)}
.hero-text{position:absolute;left:83px;top:134px;color:var(--white)}
.hero-text h1{font-weight:600;font-size:24px;line-height:30px}
.hero-text p{font-weight:400;font-size:24px;line-height:30px}
.donate-btn{position:absolute;left:84px;top:263px;width:123px;height:35px;background:var(--blue);border:2px solid var(--white);color:var(--white);font-size:10.5px;font-weight:700;letter-spacing:1px;display:flex;align-items:center;justify-content:center}
.lead-panel{position:absolute;left:538px;top:0;width:272px;height:346px;background:var(--panel);padding:6px 8px}
.callout{background:var(--blue);color:var(--white);text-align:center;height:88px;padding-top:18px}
.callout .label{font-size:10.5px;font-weight:600;letter-spacing:.5px}
.callout .phone{font-family:"Open Sans",sans-serif;font-size:18px;font-weight:600;letter-spacing:1px;margin-top:2px}
.callout .hours{font-size:8px;letter-spacing:.5px;margin-top:6px}
.form{padding:11px 9px 0;display:grid;grid-template-columns:1fr 1fr;gap:8px 7px;background:var(--white);height:250px}
.field{height:30px;border:1px solid var(--line);background:var(--white);font-family:"Open Sans",sans-serif;font-size:8.5px;color:#999;display:flex;align-items:center;justify-content:space-between;padding:0 11px}
.field.wide{grid-column:span 2}
.field.sel{margin-top:1px}
.submit{grid-column:span 2;height:35px;margin-top:6px;background:var(--blue);color:var(--white);font-family:"Open Sans",sans-serif;font-size:10.5px;font-weight:600;display:flex;align-items:center;justify-content:center}
.how-title{position:absolute;left:83px;top:467px;font-weight:300;font-size:23px;letter-spacing:1.5px;color:var(--ink)}
.step{position:absolute;top:522px;width:231px;height:184px;border:1px solid var(--line);background:var(--white)}
.step .num{position:absolute;right:26px;top:23px;width:38px;height:37px;background:var(--blue);color:var(--white);font-weight:300;font-size:22px;display:flex;align-items:center;justify-content:center}
.step svg{position:absolute;left:26px;top:26px}
.step h3{position:absolute;left:27px;top:78px;font-weight:500;font-size:14px;letter-spacing:1.5px;color:var(--ink)}
.step p{position:absolute;left:27px;top:108px;width:182px;font-size:8.6px;line-height:15px;color:var(--muted)}
.band{position:absolute;left:84px;top:754px;width:726px;height:384px;background:var(--blue);color:var(--white)}
.band h2{position:absolute;top:46px;font-weight:300;font-size:22px;letter-spacing:1.5px}
.features{position:absolute;left:43px;top:96px;width:290px;list-style:none}
.features li{position:relative;padding-left:24px;font-size:10px;line-height:15px;font-weight:400}
.features li b{font-weight:700}
.features svg{position:absolute;left:0;top:3px}
.faqs{position:absolute;left:372px;top:92px;width:312px}
.faq{height:33px;border:1px solid rgba(255,255,255,.85);margin-bottom:12px;display:flex;align-items:center;justify-content:space-between;padding:0 14px;font-size:11.5px}
.footer{position:absolute;left:0;top:1165px;width:896px;text-align:center;font-size:8.5px;color:var(--muted)}
</style>
</head>
<body>
<header class="site-nav">
  <div class="brand">Give Vehicle Hope</div>
  <nav class="menu"><span>HOME</span><span>ABOUT US</span></nav>
  <div class="nav-cta">GET STARTED</div>
</header>

<section class="hero">
  <div class="hero-photo" role="img" aria-label="Photo of a mother and child sitting on the roof of a car by the sea at dusk"></div>
  <div class="hero-text">
    <h1>Your car can make a difference!</h1>
    <p>It's free and easy!</p>
  </div>
  <div class="donate-btn">DONATE NOW!</div>
  <aside class="lead-panel">
    <div class="callout">
      <div class="label">CALL TOLL-FREE</div>
      <div class="phone">1-888-555-0142</div>
      <div class="hours">LIVE OPERATORS - 7 DAYS A WEEK</div>
    </div>
    <div class="form">
      <div class="field">First Name</div>
      <div class="field">First Name</div>
      <div class="field wide">Email Address*</div>
      <div class="field wide">Phone</div>
      <div class="field sel">Choose Year <svg width="9" height="6" viewBox="0 0 9 6"><path d="M1 1l3.5 3.5L8 1" fill="none" stroke="#999" stroke-width="1"/></svg></div>
      <div class="field sel">Choose Make <svg width="9" height="6" viewBox="0 0 9 6"><path d="M1 1l3.5 3.5L8 1" fill="none" stroke="#999" stroke-width="1"/></svg></div>
      <div class="field">Vehicle Model <svg width="9" height="6" viewBox="0 0 9 6"><path d="M1 1l3.5 3.5L8 1" fill="none" stroke="#999" stroke-width="1"/></svg></div>
      <div class="field">ZipCode <svg width="6" height="6" viewBox="0 0 6 6"><path d="M1 5L5 1" stroke="#bbb" stroke-width="1"/></svg></div>
      <div class="submit">Click to Donate Your Car</div>
    </div>
  </aside>
</section>

<h2 class="how-title">How It Works</h2>

<article class="step" style="left:83px">
  <svg width="32" height="32" viewBox="0 0 32 32"><path d="M7 3l5 1 2 7-3 3c2 4 4 6 8 8l3-3 7 2 1 5-3 3C16 29 4 17 4 6z" fill="none" stroke="var(--blue)" stroke-width="1.6" stroke-linejoin="round"/></svg>
  <div class="num">1</div>
  <h3>CALL US</h3>
  <p>Lorem ipsum dolor sit amet, consectetur adipiscing elit, sed do eiusmod tempor incididunt ut labore et dolore magna aliqua.</p>
</article>
<article class="step" style="left:332px">
  <svg width="46" height="30" viewBox="0 0 46 30"><path d="M2 22V14l9-9h24v17zM35 10h6l3 5v7h-9M8 12l5-5h6v5z" fill="none" stroke="var(--blue)" stroke-width="1.5" stroke-linejoin="round"/><rect x="28" y="7" width="4" height="5" fill="none" stroke="var(--blue)" stroke-width="1.2"/><circle cx="11" cy="24" r="3" fill="#fff" stroke="var(--blue)" stroke-width="1.5"/><circle cx="38" cy="24" r="3" fill="#fff" stroke="var(--blue)" stroke-width="1.5"/></svg>
  <div class="num">2</div>
  <h3>WE TOW IT</h3>
  <p>Lorem ipsum dolor sit amet, consectetur adipiscing elit, sed do eiusmod tempor incididunt ut labore et dolore magna aliqua.</p>
</article>
<article class="step" style="left:581px">
  <svg width="32" height="32" viewBox="0 0 32 32"><path d="M3 3h24v15M3 3v25h16" fill="none" stroke="var(--blue)" stroke-width="1.5"/><path d="M7 9h3M13 9h10M7 14h3M13 14h10M7 19h3M13 19h6" stroke="var(--blue)" stroke-width="1.4"/><path d="M20 24l3 3 6-7" fill="none" stroke="var(--blue)" stroke-width="1.6"/></svg>
  <div class="num">3</div>
  <h3>TAX RIGHT OFF</h3>
  <p>Lorem ipsum dolor sit amet, consectetur adipiscing elit, sed do eiusmod tempor incididunt ut labore et dolore magna aliqua.</p>
</article>

<section class="band">
  <h2 style="left:43px">What We Do?</h2>
  <ul class="features">
    <li style="margin-bottom:14px"><svg width="12" height="10" viewBox="0 0 12 10"><path d="M1 5l3.5 3.5L11 1" fill="none" stroke="#fff" stroke-width="1.8"/></svg><b>Free Local Towing</b>: Running or not, Any Condition &amp; Pickup Anywhere.</li>
    <li style="margin-bottom:17px"><svg width="12" height="10" viewBox="0 0 12 10"><path d="M1 5l3.5 3.5L11 1" fill="none" stroke="#fff" stroke-width="1.8"/></svg><b>Fast Pickup:</b> Same Day to 24 Hours.</li>
    <li style="margin-bottom:19px"><svg width="12" height="10" viewBox="0 0 12 10"><path d="M1 5l3.5 3.5L11 1" fill="none" stroke="#fff" stroke-width="1.8"/></svg><b>Income Tax Deduction:</b> We issue you an IRS tax receipt &amp; offer the largest resale network to get you the highest tax write-off possible.</li>
    <li style="margin-bottom:26px"><svg width="12" height="10" viewBox="0 0 12 10"><path d="M1 5l3.5 3.5L11 1" fill="none" stroke="#fff" stroke-width="1.8"/></svg><b>No Paperwork Hassles:</b> We take any car and handle everything: DMV, Smog, &amp; IRS paperwork.</li>
    <li><svg width="12" height="10" viewBox="0 0 12 10"><path d="M1 5l3.5 3.5L11 1" fill="none" stroke="#fff" stroke-width="1.8"/></svg><b>Car donations help fund programs:</b> And benefit Bright Path Kids Foundation. An IRS 501(c)3 nonprofit organization.</li>
  </ul>
  <h2 style="left:372px">FAQs</h2>
  <div class="faqs">
    <div class="faq">What types of vehicles can be donated?<span>+</span></div>
    <div class="faq">If my vehicle is not running, can I still donate?<span>+</span></div>
    <div class="faq">What paperwork do I need to donate my vehicle?<span>+</span></div>
    <div class="faq">Is my donated vehicle tax -deductible?<span>+</span></div>
    <div class="faq">What areas do you service?<span>+</span></div>
  </div>
</section>

<footer class="footer">Copyright © 2017. Give Vehicle Hope All Rights Reserved</footer>
</body>
</html>
```